Agriculture farming Hemp and CBD

The logo is in works with your company now, should be ready in a few days. We have our Domain (thequillmarkfarms.com) We would like to see incorporated seed to growth, but not necessary. we would like to nature colors and some black and green. we have our farm and will be growing and selling HEMP and CBD we are based in the state of Virginia. Would like to incorporate the words pause, play, rewind if possible but not necessary.

Target Market(s)

20 years old to elderly

Coding

Coded - Design and coding required

Number of Pages Required

3 page

Font styles to use
Serif

Requirements
Must have
• I'm not sure on the must haves, we are open to any ideas, we would definitely like to see Hemp and CBD included, may the life cycle of seed to plant. We must have a pop up asking if you are 20 years old before they can enter our site and to view or purchase our product. I want the design to be totally different than what i uploaded.
Nice to have
• Would like to see natural colors as well as black and green
Should not have
• I want

```html
<!DOCTYPE html>
<html lang="en">
<head>
<meta charset="utf-8">
<title>The Quillmark Farms – Home</title>
<link href="https://fonts.googleapis.com/css2?family=Poppins:wght@400;500;600&display=swap" rel="stylesheet">
<style>
:root{
  --green:#00b12b;
  --green-deep:#008f22;
  --ink:#111111;
  --night:#15171a;
  --text:#1c1c1c;
  --muted:#8c8c8c;
  --mist:#f4f4f4;
  --card:#f1f1f1;
  --backdrop:#ececec;
  --white:#ffffff;
}
*{box-sizing:border-box;margin:0;padding:0}
html,body{width:1200px;height:2248px;overflow:hidden;background:var(--backdrop);font-family:"Poppins",sans-serif;color:var(--text)}
.stage{position:relative;width:1200px;height:2248px}
.page{position:absolute;top:57px;width:592px;height:2445px;background:var(--white);transform:scale(.8727);transform-origin:0 0;overflow:hidden;box-shadow:0 4px 18px rgba(0,0,0,.18)}
.page--gate{left:60px}
.page--open{left:624px}
.abs{position:absolute}

/* nav */
.nav{position:absolute;left:0;top:0;width:592px;height:42px;background:var(--ink)}
.brand{position:absolute;left:44px;top:13px;color:var(--white);font-size:11px;font-weight:600;letter-spacing:.1px}
.menu{position:absolute;left:235px;top:15px;display:flex;gap:13px;font-size:7.5px;color:#d8d8d8}
.menu .is-active{color:var(--green)}
.tools{position:absolute;left:518px;top:15px;display:flex;gap:14px}

/* hero */
.hero-photo{position:absolute;left:0;top:42px;width:592px;height:303px;background:radial-gradient(ellipse at 50% 75%,#2f3a22 0%,#1b1f1a 35%,#0e0f12 75%)}
.hero-title{position:absolute;left:0;top:104px;width:592px;text-align:center;color:var(--white);font-size:31px;font-weight:500}
.btn-shop{position:absolute;left:246px;top:156px;width:99px;height:25px;border-radius:13px;background:var(--green);color:var(--white);font-size:8.5px;font-weight:600;text-align:center;line-height:25px}

/* features */
.feature{position:absolute;top:383px;width:80px;text-align:center;font-size:7px;font-weight:500}
.feature svg{display:block;margin:0 auto 8px}

/* welcome */
.rule{position:absolute;height:2px;width:40px;background:var(--green)}
.rule--white{background:var(--white)}
.welcome-title{position:absolute;left:44px;top:496px;font-size:18px;font-weight:500;line-height:24px;color:var(--ink)}
.copy{font-size:6.6px;line-height:15.5px;color:var(--muted)}
.welcome-copy{position:absolute;left:291px;top:482px;width:256px;text-align:justify}

/* steps */
.step{position:absolute;width:160px}
.step h3{font-size:10px;font-weight:500;color:var(--ink);margin-bottom:6px}
.step .copy{line-height:14px}
.photo{position:absolute}

/* what we do */
.green-band{position:absolute;left:0;top:823px;width:592px;height:660px;background:radial-gradient(ellipse at 30% 30%,#12c23a 0%,var(--green) 45%,#00a427 100%)}
.section-title{position:absolute;left:0;width:592px;text-align:center;font-size:18px;font-weight:500;color:var(--ink)}
.section-title--light{color:var(--white)}
.service{position:absolute;color:var(--white);width:230px}
.service h3{font-size:15px;font-weight:500;line-height:19px;margin-bottom:9px}
.service .copy{color:#eafbe9;line-height:15.5px}
.disc{position:absolute;border-radius:50%}

/* products */
.product{position:absolute;top:1572px;width:121px;text-align:center}
.product .frame{height:128px;background:var(--card)}
.product h4{font-size:7.5px;font-weight:600;margin-top:7px;color:var(--ink)}
.product p{font-size:7.5px;color:var(--green);margin-top:2px}
.pager{position:absolute;top:1747px;width:17px;height:17px;border:1px solid #cfcfcf;background:var(--white);font-size:8px;line-height:15px;text-align:center;color:#777}

/* blog */
.blog-band{position:absolute;left:0;top:1812px;width:592px;height:320px;background:var(--mist)}
.post{position:absolute;top:1907px;width:163px}
.post .photo{position:relative;height:116px}
.date{position:absolute;left:0;bottom:0;width:37px;height:38px;background:var(--green);color:var(--white);font-size:9px;font-weight:500;line-height:11px;text-align:center;padding-top:8px}
.post h4{font-size:9.6px;font-weight:500;margin-top:8px;color:var(--ink)}
.post .copy{line-height:11px;font-size:6px;margin-top:4px}
.more{font-size:6.5px;color:var(--green);margin-top:4px;font-weight:500}

/* newsletter */
.news-photo{position:absolute;left:0;top:2132px;width:592px;height:210px;background:radial-gradient(ellipse at 80% 40%,#3a5a2a 0%,#1d2b16 45%,#0c100b 85%)}
.field{position:absolute;left:179px;width:231px;height:19px;background:rgba(0,0,0,.55);color:#e5e5e5;font-size:6.8px;padding:5px 11px}
.btn-sign{position:absolute;left:179px;top:2272px;width:231px;height:21px;background:var(--green);color:var(--white);font-size:7.5px;font-weight:600;text-align:center;line-height:21px}

/* footer */
.social{position:absolute;top:2376px;left:272px;display:flex;gap:13px}
.social span{width:6px;height:6px;border-radius:50%;background:#777}
.foot-links{position:absolute;top:2400px;left:0;width:592px;display:flex;justify-content:center;gap:19px;font-size:7px;color:#666}
.legal{position:absolute;top:2419px;left:0;width:592px;text-align:center;font-size:6.5px;color:#777}

/* age gate */
.age-gate{position:absolute;inset:0;background:rgba(0,0,0,.55)}
.age-dialog{position:absolute;left:167px;top:95px;width:258px;height:165px;background:var(--green)}
.age-dialog h2{position:absolute;top:52px;left:0;width:258px;text-align:center;color:var(--white);font-size:14px;font-weight:600}
.age-close{position:absolute;right:7px;top:2px;color:var(--white);font-size:13px;font-weight:600}
.choice{position:absolute;top:88px;width:62px;height:21px;border-radius:11px;font-size:7.5px;font-weight:500;text-align:center;line-height:21px}
.choice--yes{left:65px;background:var(--ink);color:var(--white)}
.choice--no{left:131px;background:var(--white);color:var(--green)}
</style>
</head>
<body>
<div class="stage">

<!-- ================= gated state ================= -->
<div class="page page--gate">
  <header class="nav">
    <div class="brand">thequillmarkfarms.com</div>
    <nav class="menu"><span class="is-active">Home</span><span>About Us</span><span>Products</span><span>Category</span><span>Blog</span><span>Contact Us</span></nav>
    <div class="tools">
      <svg width="8" height="8" viewBox="0 0 10 10"><path d="M0 1h2l1.5 5h5L10 2.5H3" fill="none" stroke="#ddd" stroke-width="1.2"/><circle cx="4" cy="8.6" r="1" fill="#ddd"/><circle cx="8" cy="8.6" r="1" fill="#ddd"/></svg>
      <svg width="8" height="8" viewBox="0 0 10 10"><circle cx="4.2" cy="4.2" r="3" fill="none" stroke="#ddd" stroke-width="1.4"/><path d="M6.5 6.5L9.5 9.5" stroke="#ddd" stroke-width="1.5"/></svg>
    </div>
  </header>
  <div class="hero-photo" role="img" aria-label="Three young hemp seedlings in soil plugs on a dark background"></div>
  <h1 class="hero-title">Pause, Play, Rewind</h1>
  <div class="btn-shop">Shop Now</div>

  <div class="feature" style="left:34px"><svg width="44" height="44" viewBox="0 0 44 44"><path d="M6 40C8 18 22 6 42 6 40 26 28 38 10 36Z" fill="#4cc15a"/><path d="M4 42L30 16" stroke="#fff" stroke-width="1.5"/></svg>100% Organic</div>
  <div class="feature" style="left:147px"><svg width="44" height="44" viewBox="0 0 44 44"><circle cx="22" cy="22" r="19" fill="#4cc15a"/><path d="M13 22l6 6 12-12" fill="none" stroke="#fff" stroke-width="3"/></svg>100% Gurantee</div>
  <div class="feature" style="left:260px"><svg width="44" height="44" viewBox="0 0 44 44"><path d="M22 3C14 16 9 22 9 29a13 13 0 0 0 26 0C35 22 30 16 22 3Z" fill="#4cc15a"/></svg>3rd party Tested</div>
  <div class="feature" style="left:372px"><svg width="44" height="44" viewBox="0 0 44 44"><circle cx="22" cy="22" r="19" fill="#4cc15a"/><circle cx="22" cy="22" r="15" fill="none" stroke="#c9efcf" stroke-width="1.2"/></svg>&lt;.3% THC</div>
  <div class="feature" style="left:484px"><svg width="44" height="44" viewBox="0 0 44 44"><circle cx="22" cy="22" r="19" fill="#4cc15a"/><circle cx="22" cy="22" r="15" fill="none" stroke="#c9efcf" stroke-width="1.2"/></svg>NON GMO</div>

  <div class="rule" style="left:44px;top:486px"></div>
  <h2 class="welcome-title">Welcome To<br>The Quillmark Farms</h2>
  <p class="copy welcome-copy">Lorem ipsum dolor sit amet, consectetur adipiscing elit, sed do eiusmod tempor incididunt ut labore et dolore magna aliqua. Ut enim ad minim veniam, quis nostrud exercitation ullamco laboris nisi ut aliquip ex ea commodo consequat. Duis aute irure dolor in reprehenderit in voluptate velit esse cillum dolore eu fugiat nulla pariatur.</p>

  <div class="step" style="left:44px;top:600px"><h3>01.Design &amp; Planting</h3><p class="copy">Lorem ipsum dolor sit amet,<br>consectetur adipiscing elit, sed do eiusmod tempor incididunt ut labore et dolore magna aliqua.</p></div>
  <div class="step" style="left:214px;top:631px"><h3>02.Garden Care</h3><p class="copy">Lorem ipsum dolor sit amet,<br>consectetur adipiscing elit, sed do eiusmod tempor incididunt ut labore et dolore magna aliqua.</p></div>
  <div class="step" style="left:384px;top:600px"><h3>03.Smart Planning</h3><p class="copy">Lorem ipsum dolor sit amet,<br>consectetur adipiscing elit, sed do eiusmod tempor incididunt ut labore et dolore magna aliqua.</p></div>

  <div class="green-band" role="img" aria-label="Green band with large hemp leaves in the background"></div>
  <div class="photo" style="left:44px;top:687px;width:163px;height:178px;background:linear-gradient(160deg,#7bbf6a,#2e6a2a)" role="img" aria-label="Close-up of a hemp leaf"></div>
  <div class="photo" style="left:214px;top:718px;width:163px;height:178px;background:linear-gradient(180deg,#dfe8e2 0%,#9fbf8a 35%,#3f7a2c 100%)" role="img" aria-label="Rows of hemp plants inside a greenhouse"></div>
  <div class="photo" style="left:384px;top:687px;width:163px;height:178px;background:linear-gradient(135deg,#7a5a3c,#c89a68 60%,#e8d2b4)" role="img" aria-label="Hand placing a seed into a soil pot with tweezers"></div>

  <div class="rule rule--white" style="left:276px;top:942px"></div>
  <h2 class="section-title section-title--light" style="top:952px">What We Do</h2>
  <div class="service" style="left:86px;top:1026px"><h3>Agriculture<br>farming Hemp</h3><p class="copy">Lorem ipsum dolor sit amet, consectetur adipiscing elit, sed do eiusmod tempor incididunt ut labore et dolore magna aliqua. Ut enim ad minim veniam, quis nostrud exercitation ullamco laboris nisi ut aliquip ex ea commodo consequat. Duis aute irure dolor in reprehenderit in voluptate velit esse cillum dolore eu fugiat nulla pariatur.</p></div>
  <div class="disc" style="left:281px;top:985px;width:224px;height:224px;background:radial-gradient(circle at 50% 40%,#6b6a66,#2a2b2e 70%)" role="img" aria-label="Hemp flower bud with frosty trichomes"></div>
  <div class="disc" style="left:86px;top:1211px;width:224px;height:224px;background:radial-gradient(circle at 50% 45%,#4f8a3a,#2b5a22 70%,#d2c39a)" role="img" aria-label="Young CBD hemp plant seen from above"></div>
  <div class="service" style="left:283px;top:1252px"><h3>Agriculture<br>farming CBD</h3><p class="copy">Lorem ipsum dolor sit amet, consectetur adipiscing elit, sed do eiusmod tempor incididunt ut labore et dolore magna aliqua. Ut enim ad minim veniam, quis nostrud exercitation ullamco laboris nisi ut aliquip ex ea commodo consequat. Duis aute irure dolor in reprehenderit in voluptate velit esse cillum dolore eu fugiat nulla pariatur.</p></div>

  <div class="rule" style="left:276px;top:1530px"></div>
  <h2 class="section-title" style="top:1540px">Our Products</h2>
  <div class="product" style="left:44px"><div class="frame" role="img" aria-label="Dried hemp flower bud" style="background:radial-gradient(circle at 50% 50%,#a58a3c 0 22%,var(--card) 40%)"></div><h4>Product Name</h4><p>$41.00</p></div>
  <div class="product" style="left:171px"><div class="frame" role="img" aria-label="Dried hemp flower bud" style="background:radial-gradient(ellipse at 50% 52%,#6f7a3a 0 22%,var(--card) 40%)"></div><h4>Product Name</h4><p>$41.00</p></div>
  <div class="product" style="left:298px"><div class="frame" role="img" aria-label="Fresh hemp leaf sprig" style="background:radial-gradient(ellipse at 50% 50%,#6f9a5a 0 18%,var(--card) 40%)"></div><h4>Product Name</h4><p>$41.00</p></div>
  <div class="product" style="left:426px"><div class="frame" role="img" aria-label="Small dried hemp buds" style="background:radial-gradient(circle at 50% 50%,#a7a04f 0 20%,var(--card) 38%)"></div><h4>Product Name</h4><p>$41.00</p></div>
  <div class="pager" style="left:275px">‹</div><div class="pager" style="left:298px">›</div>

  <div class="blog-band"></div>
  <div class="rule" style="left:276px;top:1859px"></div>
  <h2 class="section-title" style="top:1869px">Latest Blog</h2>
  <article class="post" style="left:44px"><div class="photo" role="img" aria-label="Seedling sprouting from dark soil" style="background:linear-gradient(135deg,#1d1d1a,#4a7a38)"><div class="date">25<br>Mar</div></div><h4>Lorem ipsum dolor sit amet</h4><p class="copy">Sed ut perspiciatis unde omnis iste natus error sit voluptatem accusantium doloremque</p><p class="more">Learn More</p></article>
  <article class="post" style="left:214px"><div class="photo" role="img" aria-label="Hand inspecting a hemp leaf" style="background:linear-gradient(135deg,#5d8a44,#2f5a24)"><div class="date">25<br>Mar</div></div><h4>Lorem ipsum dolor sit amet</h4><p class="copy">Sed ut perspiciatis unde omnis iste natus error sit voluptatem accusantium doloremque</p><p class="more">Learn More</p></article>
  <article class="post" style="left:384px"><div class="photo" role="img" aria-label="Gloved hands trimming a hemp plant" style="background:linear-gradient(135deg,#3f6a32,#2a6a7a)"><div class="date">25<br>Mar</div></div><h4>Lorem ipsum dolor sit amet</h4><p class="copy">Sed ut perspiciatis unde omnis iste natus error sit voluptatem accusantium doloremque</p><p class="more">Learn More</p></article>

  <div class="news-photo" role="img" aria-label="Dark background of hemp leaves"></div>
  <div class="rule" style="left:276px;top:2180px"></div>
  <h2 class="section-title section-title--light" style="top:2190px">Sign Up Our Newsletter</h2>
  <div class="field" style="top:2222px">User Name</div>
  <div class="field" style="top:2246px">Email Address</div>
  <div class="btn-sign">Sign Up</div>

  <div class="social"><span></span><span></span><span></span></div>
  <nav class="foot-links"><span>Home</span><span>About Us</span><span>Products</span><span>Category</span><span>Blog</span><span>Contact Us</span></nav>
  <p class="legal">© Copyrights 2020 The Company Name. All rights reserved.</p>

  <div class="age-gate">
    <div class="age-dialog" role="dialog" aria-label="Age check">
      <span class="age-close">×</span>
      <h2>you are 20 years old</h2>
      <span class="choice choice--yes">Yes</span>
      <span class="choice choice--no">No</span>
    </div>
  </div>
</div>

<!-- ================= open state ================= -->
<div class="page page--open">
  <header class="nav">
    <div class="brand">thequillmarkfarms.com</div>
    <nav class="menu"><span class="is-active">Home</span><span>About Us</span><span>Products</span><span>Category</span><span>Blog</span><span>Contact Us</span></nav>
    <div class="tools">
      <svg width="8" height="8" viewBox="0 0 10 10"><path d="M0 1h2l1.5 5h5L10 2.5H3" fill="none" stroke="#ddd" stroke-width="1.2"/><circle cx="4" cy="8.6" r="1" fill="#ddd"/><circle cx="8" cy="8.6" r="1" fill="#ddd"/></svg>
      <svg width="8" height="8" viewBox="0 0 10 10"><circle cx="4.2" cy="4.2" r="3" fill="none" stroke="#ddd" stroke-width="1.4"/><path d="M6.5 6.5L9.5 9.5" stroke="#ddd" stroke-width="1.5"/></svg>
    </div>
  </header>
  <div class="hero-photo" role="img" aria-label="Three young hemp seedlings in soil plugs on a dark background"></div>
  <h1 class="hero-title">Pause, Play, Rewind</h1>
  <div class="btn-shop">Shop Now</div>

  <div class="feature" style="left:34px"><svg width="44" height="44" viewBox="0 0 44 44"><path d="M6 40C8 18 22 6 42 6 40 26 28 38 10 36Z" fill="#4cc15a"/><path d="M4 42L30 16" stroke="#fff" stroke-width="1.5"/></svg>100% Organic</div>
  <div class="feature" style="left:147px"><svg width="44" height="44" viewBox="0 0 44 44"><circle cx="22" cy="22" r="19" fill="#4cc15a"/><path d="M13 22l6 6 12-12" fill="none" stroke="#fff" stroke-width="3"/></svg>100% Gurantee</div>
  <div class="feature" style="left:260px"><svg width="44" height="44" viewBox="0 0 44 44"><path d="M22 3C14 16 9 22 9 29a13 13 0 0 0 26 0C35 22 30 16 22 3Z" fill="#4cc15a"/></svg>3rd party Tested</div>
  <div class="feature" style="left:372px"><svg width="44" height="44" viewBox="0 0 44 44"><circle cx="22" cy="22" r="19" fill="#4cc15a"/><circle cx="22" cy="22" r="15" fill="none" stroke="#c9efcf" stroke-width="1.2"/></svg>&lt;.3% THC</div>
  <div class="feature" style="left:484px"><svg width="44" height="44" viewBox="0 0 44 44"><circle cx="22" cy="22" r="19" fill="#4cc15a"/><circle cx="22" cy="22" r="15" fill="none" stroke="#c9efcf" stroke-width="1.2"/></svg>NON GMO</div>

  <div class="rule" style="left:44px;top:486px"></div>
  <h2 class="welcome-title">Welcome To<br>The Quillmark Farms</h2>
  <p class="copy welcome-copy">Lorem ipsum dolor sit amet, consectetur adipiscing elit, sed do eiusmod tempor incididunt ut labore et dolore magna aliqua. Ut enim ad minim veniam, quis nostrud exercitation ullamco laboris nisi ut aliquip ex ea commodo consequat. Duis aute irure dolor in reprehenderit in voluptate velit esse cillum dolore eu fugiat nulla pariatur.</p>

  <div class="step" style="left:44px;top:600px"><h3>01.Design &amp; Planting</h3><p class="copy">Lorem ipsum dolor sit amet,<br>consectetur adipiscing elit, sed do eiusmod tempor incididunt ut labore et dolore magna aliqua.</p></div>
  <div class="step" style="left:214px;top:631px"><h3>02.Garden Care</h3><p class="copy">Lorem ipsum dolor sit amet,<br>consectetur adipiscing elit, sed do eiusmod tempor incididunt ut labore et dolore magna aliqua.</p></div>
  <div class="step" style="left:384px;top:600px"><h3>03.Smart Planning</h3><p class="copy">Lorem ipsum dolor sit amet,<br>consectetur adipiscing elit, sed do eiusmod tempor incididunt ut labore et dolore magna aliqua.</p></div>

  <div class="green-band" role="img" aria-label="Green band with large hemp leaves in the background"></div>
  <div class="photo" style="left:44px;top:687px;width:163px;height:178px;background:linear-gradient(160deg,#7bbf6a,#2e6a2a)" role="img" aria-label="Close-up of a hemp leaf"></div>
  <div class="photo" style="left:214px;top:718px;width:163px;height:178px;background:linear-gradient(180deg,#dfe8e2 0%,#9fbf8a 35%,#3f7a2c 100%)" role="img" aria-label="Rows of hemp plants inside a greenhouse"></div>
  <div class="photo" style="left:384px;top:687px;width:163px;height:178px;background:linear-gradient(135deg,#7a5a3c,#c89a68 60%,#e8d2b4)" role="img" aria-label="Hand placing a seed into a soil pot with tweezers"></div>

  <div class="rule rule--white" style="left:276px;top:942px"></div>
  <h2 class="section-title section-title--light" style="top:952px">What We Do</h2>
  <div class="service" style="left:86px;top:1026px"><h3>Agriculture<br>farming Hemp</h3><p class="copy">Lorem ipsum dolor sit amet, consectetur adipiscing elit, sed do eiusmod tempor incididunt ut labore et dolore magna aliqua. Ut enim ad minim veniam, quis nostrud exercitation ullamco laboris nisi ut aliquip ex ea commodo consequat. Duis aute irure dolor in reprehenderit in voluptate velit esse cillum dolore eu fugiat nulla pariatur.</p></div>
  <div class="disc" style="left:281px;top:985px;width:224px;height:224px;background:radial-gradient(circle at 50% 40%,#6b6a66,#2a2b2e 70%)" role="img" aria-label="Hemp flower bud with frosty trichomes"></div>
  <div class="disc" style="left:86px;top:1211px;width:224px;height:224px;background:radial-gradient(circle at 50% 45%,#4f8a3a,#2b5a22 70%,#d2c39a)" role="img" aria-label="Young CBD hemp plant seen from above"></div>
  <div class="service" style="left:283px;top:1252px"><h3>Agriculture<br>farming CBD</h3><p class="copy">Lorem ipsum dolor sit amet, consectetur adipiscing elit, sed do eiusmod tempor incididunt ut labore et dolore magna aliqua. Ut enim ad minim veniam, quis nostrud exercitation ullamco laboris nisi ut aliquip ex ea commodo consequat. Duis aute irure dolor in reprehenderit in voluptate velit esse cillum dolore eu fugiat nulla pariatur.</p></div>

  <div class="rule" style="left:276px;top:1530px"></div>
  <h2 class="section-title" style="top:1540px">Our Products</h2>
  <div class="product" style="left:44px"><div class="frame" role="img" aria-label="Dried hemp flower bud" style="background:radial-gradient(circle at 50% 50%,#a58a3c 0 22%,var(--card) 40%)"></div><h4>Product Name</h4><p>$41.00</p></div>
  <div class="product" style="left:171px"><div class="frame" role="img" aria-label="Dried hemp flower bud" style="background:radial-gradient(ellipse at 50% 52%,#6f7a3a 0 22%,var(--card) 40%)"></div><h4>Product Name</h4><p>$41.00</p></div>
  <div class="product" style="left:298px"><div class="frame" role="img" aria-label="Fresh hemp leaf sprig" style="background:radial-gradient(ellipse at 50% 50%,#6f9a5a 0 18%,var(--card) 40%)"></div><h4>Product Name</h4><p>$41.00</p></div>
  <div class="product" style="left:426px"><div class="frame" role="img" aria-label="Small dried hemp buds" style="background:radial-gradient(circle at 50% 50%,#a7a04f 0 20%,var(--card) 38%)"></div><h4>Product Name</h4><p>$41.00</p></div>
  <div class="pager" style="left:275px">‹</div><div class="pager" style="left:298px">›</div>

  <div class="blog-band"></div>
  <div class="rule" style="left:276px;top:1859px"></div>
  <h2 class="section-title" style="top:1869px">Latest Blog</h2>
  <article class="post" style="left:44px"><div class="photo" role="img" aria-label="Seedling sprouting from dark soil" style="background:linear-gradient(135deg,#1d1d1a,#4a7a38)"><div class="date">25<br>Mar</div></div><h4>Lorem ipsum dolor sit amet</h4><p class="copy">Sed ut perspiciatis unde omnis iste natus error sit voluptatem accusantium doloremque</p><p class="more">Learn More</p></article>
  <article class="post" style="left:214px"><div class="photo" role="img" aria-label="Hand inspecting a hemp leaf" style="background:linear-gradient(135deg,#5d8a44,#2f5a24)"><div class="date">25<br>Mar</div></div><h4>Lorem ipsum dolor sit amet</h4><p class="copy">Sed ut perspiciatis unde omnis iste natus error sit voluptatem accusantium doloremque</p><p class="more">Learn More</p></article>
  <article class="post" style="left:384px"><div class="photo" role="img" aria-label="Gloved hands trimming a hemp plant" style="background:linear-gradient(135deg,#3f6a32,#2a6a7a)"><div class="date">25<br>Mar</div></div><h4>Lorem ipsum dolor sit amet</h4><p class="copy">Sed ut perspiciatis unde omnis iste natus error sit voluptatem accusantium doloremque</p><p class="more">Learn More</p></article>

  <div class="news-photo" role="img" aria-label="Dark background of hemp leaves"></div>
  <div class="rule" style="left:276px;top:2180px"></div>
  <h2 class="section-title section-title--light" style="top:2190px">Sign Up Our Newsletter</h2>
  <div class="field" style="top:2222px">User Name</div>
  <div class="field" style="top:2246px">Email Address</div>
  <div class="btn-sign">Sign Up</div>

  <div class="social"><span></span><span></span><span></span></div>
  <nav class="foot-links"><span>Home</span><span>About Us</span><span>Products</span><span>Category</span><span>Blog</span><span>Contact Us</span></nav>
  <p class="legal">© Copyrights 2020 The Company Name. All rights reserved.</p>
</div>

</div>
</body>
</html>
```